Torvane PT Business Card

I need the card to be bright/bold colours to stand out amongst others.
It needs to have my company logo.
I was not interested in pictures etc just a layout that attracts attention.

I have attached my old design which is very plain. I also needed change the contact details. And my description changed to Personal Trainer
Phone 0427391058
Facebook Torvane PT
No email address please, no street address.
And only Torvane PT (Please remove anything to do with Torvane Supplements)

```html
<!DOCTYPE html>
<html lang="en">
<head>
<meta charset="utf-8">
<title>Torvane PT Business Card</title>
<link href="https://fonts.googleapis.com/css2?family=Open+Sans:wght@400;600;800&display=swap" rel="stylesheet">
<style>
  :root {
    --backdrop: #e9ecef;
    --card-white: #ffffff;
    --brand-blue: #1fa6d8;
    --deep-blue: #1389c2;
    --brand-yellow: #f2d900;
    --ink-blue: #1a9bd0;
  }
  * { margin: 0; padding: 0; box-sizing: border-box; }
  html, body {
    width: 1200px; height: 780px; overflow: hidden;
    background: var(--backdrop);
    font-family: "Open Sans", sans-serif;
  }
  .card {
    position: absolute; left: 100px; top: 105px;
    width: 1000px; height: 570px;
    background: var(--card-white);
    border-radius: 34px;
    overflow: hidden;
    box-shadow: 0 10px 30px rgba(0,0,0,0.12);
  }
  .card-art { position: absolute; inset: 0; }
  .brand {
    position: absolute; left: 80px; top: 235px;
    display: flex; align-items: center; gap: 12px;
  }
  .brand-name {
    font-weight: 800; font-size: 62px; letter-spacing: 1px;
    color: var(--brand-yellow); line-height: 1; white-space: nowrap;
  }
  .brand-mark {
    width: 18px; height: 18px; border-radius: 50%;
    background: var(--brand-yellow);
  }
  .holder {
    position: absolute; left: 470px; top: 46px;
  }
  .holder-name {
    font-weight: 600; font-size: 34px; color: var(--ink-blue);
    letter-spacing: 1px; line-height: 1.1; white-space: nowrap;
  }
  .holder-role {
    font-weight: 400; font-size: 24px; color: var(--brand-yellow);
    margin-left: 40px; white-space: nowrap;
  }
  .contact-icons {
    position: absolute; right: 50px; top: 170px;
    display: flex; gap: 8px;
  }
  .contact-icon {
    width: 34px; height: 34px; border-radius: 6px;
    background: var(--brand-yellow);
    display: flex; align-items: center; justify-content: center;
  }
  .contact-list {
    position: absolute; right: 50px; top: 226px;
    list-style: none; text-align: right;
    color: var(--card-white); font-size: 27px; line-height: 1.5;
    white-space: nowrap;
  }
</style>
</head>
<body>
  <div class="card">
    <svg class="card-art" viewBox="0 0 1000 570" width="1000" height="570" aria-hidden="true">
      <path d="M370 570 C520 560 600 380 680 230 C730 130 790 40 860 0 L1000 0 L1000 570 Z" fill="var(--brand-blue)"/>
      <path d="M430 570 C560 540 620 360 700 220 C750 130 800 60 870 0 L1000 0 L1000 570 Z" fill="var(--deep-blue)" opacity="0.35"/>
      <path d="M420 560 C540 520 610 360 690 220 C740 140 790 70 840 25" fill="none" stroke="var(--card-white)" stroke-width="6"/>
      <path d="M330 570 C480 540 560 430 600 300 C570 420 470 520 360 570 Z" fill="var(--brand-yellow)"/>
    </svg>

    <div class="brand">
      <span class="brand-name">TORVANE PT</span>
      <span class="brand-mark"></span>
    </div>

    <div class="holder">
      <div class="holder-name">DEAN HARLOW</div>
      <div class="holder-role">Personal Trainer</div>
    </div>

    <div class="contact-icons">
      <span class="contact-icon">
        <svg width="20" height="20" viewBox="0 0 24 24"><path d="M6.6 10.8a15 15 0 0 0 6.6 6.6l2.2-2.2a1 1 0 0 1 1-.25 11.4 11.4 0 0 0 3.6.57 1 1 0 0 1 1 1V20a1 1 0 0 1-1 1A17 17 0 0 1 3 4a1 1 0 0 1 1-1h3.5a1 1 0 0 1 1 1c0 1.25.2 2.45.57 3.6a1 1 0 0 1-.25 1z" fill="var(--deep-blue)"/></svg>
      </span>
      <span class="contact-icon">
        <svg width="16" height="16" viewBox="0 0 16 16"><rect x="2" y="2" width="12" height="12" fill="var(--deep-blue)"/></svg>
      </span>
    </div>

    <ul class="contact-list">
      <li>0427391058</li>
      <li>Torvane PT</li>
    </ul>
  </div>
</body>
</html>
```